Crestline Folio Network Presents… CFNMerit.example

I. The purpose of the phase1 is to gain access to (and control of) scholastic academic works that had been written and authored by students, but only after they have been corrected (vetted), by education professionals and returned to the student as corrected documents. It is my goal to push the CFN Merit Annual as inducements to have students turn over these papers and receive recognition and authorship, for these intellectual works.

Target Market(s)

university students
high school students

Number of Pages Required

2 page

Font styles to use
Serif
Sans Serif

Colors

Designer to choose colors to be used in the design.

Requirements
Must have
• must include this or similar language.
• Crestline Folio Network Presents…
• CFNMerit.example
• Here is the assemblage of your academic successes. We collect and archive your written academic achievements, you’re “A” graded as correct, written assignments throughout the year, and when it’s over, we amass your academic documents into a bound book… your Scholar Summit Annual.
• You study hard and work hard all year trying to achieve the highest grades possible. At the end of the year, semester, or term you will have lasting proof to show what you did to achieve your academic excellence… and in book form too!
• Consider this the perfect gift to yourself to celebrate your ascendency and to showcase all of the hard work that you have put into getting to the next step on the ladder to success, your success.
• One good thing about this is that you don’t have to do any extra work to write your book. Once your written assignment has been reviewed, graded by an education authority and returned to you, all you do is to submit it to your registered account with us, add a brief description or special detail and we will add it to your database to build your success story.
• Our mission here is to track and highlight your academic successes. We want to honor and immortalize you through your academic “A” papers. Currently, once your term papers, research papers, writing assignments, book reports, studies, critiques, essays, theses, dissertations and the like, have been graded and returned back to you they soon become of no further value to you. But now with the Scholar Summit Annual you have a system available to you that can and will create a lasting record or Yearbook to catalogue what molded you into the intellectual that you have become. Once your academic papers have been evaluated by the scholastic authority and graded accordingly, you only have to post or download these materials as they become available to you. As you repeat the process again and again the storehouse of your knowledge legacy grows exponentially and become more relevant and valuable as entries into your Scholar Summit Annual.
• Imagine if you will, if there was a written record of Kowalczyk’s early studies and writings, from before he became the Kowalczyk that we know of today, or the Pemberton’s early school and college writings? Just think of the value that these priceless gifts would hold today. Well you may say “but I’m not famous. Who would be interested in my schoolwork or assignments?” We can’t say for sure right now because the future is not known today. But we do know that years of study and research molded and shaped the Pembertons from their modest upbringing and that Kowalczyk struggled for many years trying to get his thoughts and writings accepted by the establishment before they finally realized that “e” really did equal “mc2” (e=mc2). Who Knew? But you don’t have to become famous to be relevant. What value would you place on old mementos and writings of your parents, grand or great grandparents from before Vietnam or WWIl or??? I’m sure Kinroot.example would kill to have access to these treasures. And so would your kids or descendants in future years. Yes, you are relevant and you can make a lasting difference if you create an enduring legacy. Together we can create that legacy.
• “Log on to: CFNMerit.example to comprehend what all the excitement is all about.”
• We are the vehicle to deliver your curriculum based study writings to you in the easiest and most hassle free way possible. As members of the Scholar Summit community your papers will always be available to you. Periodically this material will be compiled, configured if necessary, and formatted into book form as your personalized Scholar Summit Annual matures.
Nice to have
• very professional but student friendly graphes
Should not have
• leave out the affiliate program at this time.

```html
<!DOCTYPE html>
<html lang="en">
<head>
<meta charset="utf-8">
<title>Crestline Folio Network — Business Plan</title>
<link rel="stylesheet" href="https://fonts.googleapis.com/css2?family=Open+Sans:wght@300;400;600;700&display=swap">
<style>
  :root{
    --teal:#2e8aab;
    --teal-light:#8fc4d6;
    --ink:#1c1c1c;
    --grey-text:#6a6a6a;
    --paper:#ececec;
    --paper-cover:#e6e6e6;
    --backdrop:#f4f4f4;
    --chip:#dcdcdc;
  }
  *{box-sizing:border-box;margin:0;padding:0}
  html,body{width:1200px;height:3103px;overflow:hidden}
  body{background:var(--backdrop);font-family:"Open Sans",Arial,sans-serif;color:var(--ink);position:relative}

  .page{position:absolute;background:var(--paper)}

  /* Cover */
  .cover{left:107px;top:108px;width:990px;height:1406px;background:var(--paper-cover);overflow:hidden}
  .cover-band{position:absolute;left:0;top:0;width:100%;height:162px}
  .cover-title{position:absolute;left:96px;top:252px;font-size:70px;letter-spacing:-2.5px;line-height:1;white-space:nowrap}
  .cover-title b{font-weight:600}
  .cover-title span{font-weight:300}
  .cover-subtitle{position:absolute;left:96px;top:350px;font-size:23px;line-height:1.35;letter-spacing:-.5px}
  .cover-photo{position:absolute;left:0;top:440px;width:100%;height:966px;background:linear-gradient(160deg,#b4b4b4 0%,#7a7a7a 45%,#3e3e3e 100%)}
  .cover-overlay{position:absolute;left:0;top:440px;width:100%;height:966px}
  .cover-contact{position:absolute;left:96px;top:1094px;color:#fff;font-size:19px;line-height:31px;font-style:normal}
  .cover-date{position:absolute;right:70px;top:1250px;color:#fff;font-size:48px;font-weight:300;line-height:1;text-align:center}

  /* Inside page */
  .inside{left:95px;top:1576px;width:1012px;height:1428px}
  .conf-title{position:absolute;left:112px;top:72px;font-size:58px;font-weight:300;letter-spacing:-1px;color:#333}
  .conf-rule{position:absolute;left:112px;top:160px;width:175px;height:4px;background:var(--teal)}
  .quote-mark{position:absolute;left:150px;top:232px}
  .notice{position:absolute;left:360px;top:234px;width:545px;font-size:14.5px;line-height:23px}
  .notice-lead{font-weight:700;color:var(--ink);margin-bottom:18px}
  .notice-body{color:var(--grey-text);text-align:justify}
  .presents-line{position:absolute;left:112px;top:598px;right:112px;border-top:1px solid #bcbcbc}
  .site-chip{position:absolute;right:112px;top:586px;background:var(--chip);font-size:12px;font-weight:700;padding:2px 12px;color:#333}
  .presents{position:absolute;left:112px;top:604px;font-size:19px;color:var(--teal);text-transform:uppercase}
  .community{position:absolute;left:112px;top:634px;font-size:30px;font-weight:700;color:var(--teal);text-transform:uppercase;letter-spacing:.3px}
  .phase{position:absolute;top:695px;height:83px;width:388px;background:var(--chip);display:flex;align-items:center}
  .phase-tag{width:26px;height:100%;background:var(--teal);color:#fff;font-size:14px;font-weight:700;writing-mode:vertical-rl;transform:rotate(180deg);text-align:center}
  .phase-name{margin-left:40px;font-size:29px}
  .phase.one{left:112px}
  .phase.two{left:512px}
  .plan-body{position:absolute;left:112px;top:800px;width:788px;font-size:15.6px;line-height:22px;text-align:justify}
  .foot-rule{position:absolute;left:112px;right:112px;top:1262px;border-top:1px solid #bcbcbc}
  .goal{position:absolute;left:200px;width:612px;top:1284px;font-size:14px;line-height:21px;font-weight:700;color:var(--teal);text-align:center}
</style>
</head>
<body>

<section class="page cover">
  <svg class="cover-band" viewBox="0 0 990 162" preserveAspectRatio="none" aria-hidden="true">
    <polygon points="0,0 990,0 990,95 925,162 0,162" fill="var(--teal)"/>
  </svg>
  <h1 class="cover-title"><b>Crestline Folio</b> <span>Network</span></h1>
  <p class="cover-subtitle">Crestline Folio Network<br>(aka CFN Folios) BUSINESS PLAN</p>

  <div class="cover-photo" role="img" aria-label="Black and white photograph of a smiling graduate in cap and gown outside a campus building"></div>
  <svg class="cover-overlay" viewBox="0 0 990 966" aria-hidden="true">
    <polygon points="0,0 650,0 0,660" fill="var(--teal-light)" opacity=".82"/>
    <polygon points="640,110 690,110 210,590 160,590" fill="var(--teal)"/>
    <polygon points="330,385 340,385 0,720 0,710" fill="#fff"/>
    <polygon points="990,910 990,966 935,966" fill="var(--teal)"/>
  </svg>

  <address class="cover-contact">
    Dorian Vell<br>
    Owner<br>
    Crestline Folio Network<br>
    218 Larkfield Avenue<br>
    Brookhaven, ST 00412<br>
    Tel: (555)014-2286<br>
    URL: CrestlineFolioNetwork.example<br>
    Email: dvell@mailpost.example
  </address>
  <p class="cover-date">Nov.<br>2018</p>
</section>

<section class="page inside">
  <h2 class="conf-title">CONFIDENTIAL</h2>
  <div class="conf-rule"></div>

  <svg class="quote-mark" width="136" height="136" viewBox="0 0 136 136" aria-hidden="true">
    <path d="M8 136 V70 Q8 16 56 4 L60 20 Q34 32 34 62 H58 V136 Z" fill="#444"/>
    <path d="M78 136 V70 Q78 16 126 4 L130 20 Q104 32 104 62 H128 V136 Z" fill="#444"/>
  </svg>

  <div class="notice">
    <p class="notice-lead">No offering is made or intended by this document. Any offering of interests in Crestline Folio Network will be made only in compliance with Federal and State securities laws.</p>
    <p class="notice-body">This document includes confidential and proprietary information of and regarding Crestline Folio Network. This document is provided for informational purposes only. You may not use this document except for informational purposes, and you may not reproduce this document in whole or in part, or divulge any of its contents without the prior written consent of Crestline Folio Network. By accepting this document, you agree to be bound by these restrictions and limitations.</p>
  </div>

  <div class="presents-line"></div>
  <span class="site-chip">www.CrestlineFolioNetwork.example</span>
  <p class="presents">Crestline Folio Network presents…</p>
  <h3 class="community">The Crestline Folio Community</h3>

  <div class="phase one"><span class="phase-tag">Phase 1</span><span class="phase-name">CFNMerit.example</span></div>
  <div class="phase two"><span class="phase-tag">Phase 2</span><span class="phase-name">CFNFolios.example</span></div>

  <div class="plan-body">
    <p>Here is the assemblage of your academic successes. We collect and archive your written academic achievements, your “A” graded written assignments throughout the year, and when it’s over, we amass them into a bound book… your Scholar Summit Annual.</p>
    <p>You study hard and work hard all year trying to achieve the highest grades possible. At the end of the year, semester, or term you will have lasting proof of your academic excellence… and in book form too! Consider this the perfect gift to yourself to celebrate your ascendency and the hard work it took to reach the next step on the ladder to success, your success.</p>
    <p>You don’t have to do any extra work to write your book. Once your assignment has been graded by an education authority and returned to you, simply submit it to your registered account, add a brief description, and we add it to your database to build your success story.</p>
    <p>Our mission is to track and highlight your academic successes and to honor you through your “A” papers. Term papers, research papers, essays, theses and dissertations soon lose their value once graded; the Scholar Summit Annual turns them into a lasting record of what molded you into the intellectual you have become.</p>
    <p>Imagine a written record of Kowalczyk’s early studies, or the Pembertons’ early school writings. You don’t have to become famous to be relevant: Kinroot.example would value such treasures, and so will your kids and descendants. Together we can create that legacy.</p>
    <p>We are the vehicle to deliver your curriculum based study writings in the easiest, most hassle free way possible. As members of the Scholar Summit community your papers will always be available, compiled and formatted into book form as your personalized Scholar Summit Annual matures.</p>
  </div>

  <div class="foot-rule"></div>
  <p class="goal">Log on to: CFNMerit.example to comprehend what all the excitement is all about.</p>
</section>

</body>
</html>
```